Business Card Design

I am an Event and Wedding Planner in need of an eye catching business card featuring my logo (attached), my contact details, and my company tagline (Making every milestone simply magnificent...) I would like the tagline in font similar the logo's font.
Updates
I have just noticed that my logo has a misspelling so for the final design, I will be uploading a corrected logo as soon as I have it.
My apologies.
Reason: Waiting on a corrected logo...Occasions is misspelled and it should say Weddings not Wedding
The logo has been corrected so now Occasions is spelled correctly and it says Weddings instead of Wedding. Please use Edwardian Script ITC as the font for the tagline so it will match the logo. Thank you for your patience.
Target Market(s)
Engaged couples and people hosting milestone celebrations. 25-50 years old, predominately female
Industry/Entity Type
Business
Contact Information for Business Card
Rosalind Petty, Event Manager / Owner, Mobile: 0491 837 052, Email: rosalind@glimmerfieldevents.com.au, www.glimmerfieldevents.com.au, Making every milestone simply magnificent...

```html
<!DOCTYPE html>
<html lang="en">
<head>
<meta charset="utf-8">
<title>Glimmerfield Events – Business Card</title>
<link rel="stylesheet" href="https://fonts.googleapis.com/css2?family=Tinos&family=Pinyon+Script&display=swap">
<style>
  :root {
    --backdrop: #a3a3a3;
    --card: #ffffff;
    --ink: #1c1c1c;
    --brand-grey: #2e2e2e;
    --accent-red: #b3161b;
    --rule-grey: #3a3a3a;
  }
  * { margin: 0; padding: 0; box-sizing: border-box; }
  html, body {
    width: 1200px;
    height: 1000px;
    overflow: hidden;
    background: var(--backdrop);
  }
  .stage {
    position: relative;
    width: 1200px;
    height: 1000px;
  }
  .card {
    position: absolute;
    background: var(--card);
    border-radius: 18px;
  }

  /* Front face */
  .card-front {
    left: 116px;
    top: 62px;
    width: 686px;
    height: 418px;
  }
  .brand-name {
    position: absolute;
    left: 0;
    right: 0;
    top: 150px;
    text-align: center;
    font-family: "Tinos", "Times New Roman", serif;
    font-size: 54px;
    color: var(--brand-grey);
    letter-spacing: 1px;
  }
  .brand-rule {
    position: absolute;
    left: 178px;
    top: 230px;
    width: 356px;
    height: 2px;
    background: var(--rule-grey);
  }
  .tagline-rule {
    position: absolute;
    left: 90px;
    top: 357px;
    width: 510px;
    height: 1px;
    background: linear-gradient(to right, rgba(179,22,27,0), var(--accent-red) 50%, rgba(179,22,27,0));
  }
  .tagline {
    position: absolute;
    left: 0;
    right: 0;
    top: 362px;
    text-align: center;
    font-family: "Pinyon Script", cursive;
    font-size: 22px;
    color: var(--accent-red);
  }

  /* Back face */
  .card-back {
    left: 332px;
    top: 508px;
    width: 678px;
    height: 412px;
  }
  .contact-person {
    position: absolute;
    left: 16px;
    top: 26px;
    font-family: "Tinos", "Times New Roman", serif;
    line-height: 18px;
  }
  .person-name {
    font-size: 16px;
    color: var(--accent-red);
    text-transform: uppercase;
  }
  .person-role {
    font-size: 16px;
    color: var(--ink);
  }
  .contact-list {
    position: absolute;
    left: 16px;
    top: 152px;
    list-style: none;
    font-family: "Tinos", "Times New Roman", serif;
    font-size: 16px;
    color: var(--ink);
  }
  .contact-item {
    display: flex;
    align-items: center;
    height: 28px;
  }
  .contact-icon {
    width: 24px;
    height: 22px;
    margin-right: 11px;
    flex: none;
  }
</style>
</head>
<body>
<main class="stage">
  <section class="card card-front" aria-label="Card front">
    <h1 class="brand-name">Glimmerfield Events</h1>
    <div class="brand-rule"></div>
    <div class="tagline-rule"></div>
    <p class="tagline">Making every milestone simply magnificent...</p>
  </section>

  <section class="card card-back" aria-label="Card back">
    <div class="contact-person">
      <p class="person-name">Rosalind Petty</p>
      <p class="person-role">Event Manager / Owner</p>
    </div>
    <ul class="contact-list">
      <li class="contact-item">
        <svg class="contact-icon" viewBox="0 0 24 22" aria-hidden="true">
          <rect x="0" y="2" width="24" height="18" fill="#b3161b"/>
          <polyline points="1,3 12,13 23,3" fill="none" stroke="#fff" stroke-width="2"/>
          <line x1="1" y1="19" x2="9" y2="11" stroke="#fff" stroke-width="1.5"/>
          <line x1="23" y1="19" x2="15" y2="11" stroke="#fff" stroke-width="1.5"/>
        </svg>
        <span>rosalind@glimmerfieldevents.com.au</span>
      </li>
      <li class="contact-item">
        <svg class="contact-icon" viewBox="0 0 24 22" aria-hidden="true">
          <rect x="6" y="0.5" width="12" height="21" rx="2" fill="none" stroke="#b3161b" stroke-width="2"/>
          <line x1="7" y1="17" x2="17" y2="17" stroke="#b3161b" stroke-width="1.5"/>
        </svg>
        <span>0491 837 052</span>
      </li>
      <li class="contact-item">
        <svg class="contact-icon" viewBox="0 0 24 22" aria-hidden="true">
          <g fill="none" stroke="#b3161b" stroke-width="1.6">
            <circle cx="12" cy="11" r="10"/>
            <ellipse cx="12" cy="11" rx="4.5" ry="10"/>
            <line x1="2" y1="11" x2="22" y2="11"/>
            <path d="M4 5.5 H20 M4 16.5 H20"/>
          </g>
        </svg>
        <span>www.glimmerfieldevents.com.au</span>
      </li>
    </ul>
  </section>
</main>
</body>
</html>
```